Luxury Tea Brand Needs Packaging Design

Our team needs a luxe design replicating the shape of the attached picture for a box that will contain drawstring teabags. There is an opportunity for silver or gold reflective design

Please include a design for the

Product dimensions - 10.5x4x9 cm
things to keep in mind

- luxury design
- Mainly black with either silver or gold
- Should say pack of 100
- Should say Leaf Harbor Tea Filters

some of our products have been attached as a style reference

website is www.leafharbor.example

Target Market(s)

modern millennials

Requirements
Must have
• luxury feel
Nice to have
• shiny designs

```html
<!DOCTYPE html>
<html lang="en">
<head>
<meta charset="utf-8">
<title>Leaf Harbor Tea Filters — Box Dieline</title>
<link rel="stylesheet" href="https://fonts.googleapis.com/css2?family=Cinzel:wght@400;500&family=Cormorant+Garamond:wght@500;600&display=swap">
<style>
  :root {
    --bg: #f1f1f1;
    --bg-edge: #e4e4e4;
    --board: #000000;
    --fold: #262626;
    --gold: #e2b656;
    --gold-light: #f6dc8a;
    --gold-deep: #b9842f;
    --silver: #d9d9d9;
  }
  html, body {
    margin: 0;
    padding: 0;
    overflow: hidden;
  }
  body {
    width: 1200px;
    height: 1200px;
    background: radial-gradient(circle at 50% 50%, #fbfbfb 0%, var(--bg) 60%, var(--bg-edge) 100%);
  }
  .dieline {
    display: block;
    width: 1200px;
    height: 1200px;
  }
  .board { fill: var(--board); }
  .fold-line { stroke: var(--fold); stroke-width: 1; fill: none; }
  .brand-name {
    font-family: "Cinzel", serif;
    font-weight: 400;
    fill: var(--gold);
    letter-spacing: 1px;
  }
  .product-name {
    font-family: "Cinzel", serif;
    font-weight: 500;
    fill: var(--gold-light);
    letter-spacing: 1.5px;
  }
  .pack-label {
    font-family: "Cormorant Garamond", serif;
    font-weight: 600;
    fill: var(--gold);
    font-variant-numeric: lining-nums;
    font-feature-settings: "lnum" 1;
  }
  .web-address {
    font-family: "Cormorant Garamond", serif;
    font-weight: 500;
    fill: var(--silver);
    letter-spacing: 4px;
    font-size: 10px;
  }
  .ring { fill: none; stroke: url(#goldSheen); stroke-width: 1.6; }
  .rule { stroke: url(#goldRule); stroke-width: 1; }
  .foliage { fill: url(#foilGold); }
</style>
</head>
<body>
<svg class="dieline" viewBox="0 0 1200 1200" xmlns="http://www.w3.org/2000/svg">
  <defs>
    <linearGradient id="goldSheen" x1="0" y1="0" x2="1" y2="1">
      <stop offset="0" stop-color="#f6dc8a"/>
      <stop offset="0.5" stop-color="#e2b656"/>
      <stop offset="1" stop-color="#b9842f"/>
    </linearGradient>
    <linearGradient id="foilGold" x1="0" y1="0" x2="1" y2="1">
      <stop offset="0" stop-color="#f8de8e"/>
      <stop offset="0.45" stop-color="#e6bb5a"/>
      <stop offset="1" stop-color="#b27a2a"/>
    </linearGradient>
    <linearGradient id="goldRule" x1="0" y1="0" x2="1" y2="0">
      <stop offset="0" stop-color="#b9842f" stop-opacity="0"/>
      <stop offset="0.5" stop-color="#e2b656"/>
      <stop offset="1" stop-color="#b9842f" stop-opacity="0"/>
    </linearGradient>
    <clipPath id="boardClip">
      <path d="M134 262 Q134 242 154 242 L488 242 Q508 242 508 262 L508 960 L436 960 Q428 960 428 950 L428 886 L214 886 L214 940 Q214 960 194 960 L134 960 Z"/>
      <rect x="508" y="400" width="558" height="402"/>
      <path d="M600 802 L659 902 L659 958 L922 958 L922 902 L974 802 Z"/>
    </clipPath>
  </defs>

  <!-- Front column: tuck flap, front panel, bottom flap -->
  <path class="board" d="M134 262 Q134 242 154 242 L488 242 Q508 242 508 262 L508 960 L436 960 Q428 960 428 950 L428 886 L214 886 L214 940 Q214 960 194 960 L134 960 Z"/>
  <!-- Side panel, back panel, glue flap -->
  <rect class="board" x="508" y="400" width="558" height="402"/>
  <!-- Back bottom flap -->
  <path class="board" d="M600 802 L659 902 L659 958 L922 958 L922 902 L974 802 Z"/>

  <!-- Gold foil foliage areas -->
  <g clip-path="url(#boardClip)" opacity="0.82">
    <path class="foliage" role="img" aria-label="Gold foil leafy branch growing in from the left edge" d="M134 306 C170 300 210 350 222 410 C228 440 212 470 184 482 C160 490 140 482 134 478 Z"/>
    <path class="foliage" role="img" aria-label="Gold foil leafy branch rising from the lower right corner" d="M508 676 C470 680 430 720 412 780 C396 830 368 860 372 880 C380 900 420 890 430 900 L430 950 Q430 960 440 960 L508 960 Z"/>
    <path class="foliage" role="img" aria-label="Gold foil leafy sprig across the top of the side panel" d="M556 444 C572 420 606 400 640 400 L690 400 C690 420 672 444 640 458 C610 472 580 482 556 470 Z"/>
    <path class="foliage" role="img" aria-label="Gold foil leafy branch at the lower right of the back panel" d="M974 708 C930 708 880 734 870 770 C864 792 900 802 930 806 C940 830 930 850 932 870 L974 802 Z"/>
  </g>

  <!-- Fold lines -->
  <line class="fold-line" x1="134" y1="400" x2="508" y2="400"/>
  <line class="fold-line" x1="134" y1="802" x2="600" y2="802"/>
  <line class="fold-line" x1="508" y1="400" x2="508" y2="802"/>
  <line class="fold-line" x1="600" y1="400" x2="600" y2="802"/>
  <line class="fold-line" x1="974" y1="400" x2="974" y2="802"/>
  <line class="fold-line" x1="600" y1="802" x2="974" y2="802"/>

  <!-- Tuck flap brand (upside down) -->
  <text class="brand-name" x="322" y="322" font-size="26" text-anchor="middle" transform="rotate(180 322 322)">Leaf Harbor</text>

  <!-- Front panel -->
  <text class="brand-name" x="320" y="492" font-size="30" text-anchor="middle">Leaf Harbor</text>
  <circle class="ring" cx="320" cy="604" r="64"/>
  <text class="product-name" x="320" y="598" font-size="20" text-anchor="middle">TEA</text>
  <text class="product-name" x="320" y="621" font-size="20" text-anchor="middle">FILTERS</text>
  <line class="rule" x1="280" y1="711" x2="360" y2="711"/>
  <text class="pack-label" x="320" y="728" font-size="13" text-anchor="middle">PACK OF</text>
  <text class="pack-label" x="320" y="762" font-size="38" text-anchor="middle">100</text>
  <line class="rule" x1="280" y1="770" x2="360" y2="770"/>

  <!-- Side panel brand -->
  <text class="brand-name" x="554" y="600" font-size="25" text-anchor="middle" transform="rotate(-90 554 600) translate(0 9)">Leaf Harbor</text>

  <!-- Back panel -->
  <text class="brand-name" x="786" y="536" font-size="28" text-anchor="middle">Leaf Harbor</text>
  <circle class="ring" cx="788" cy="638" r="57"/>
  <text class="product-name" x="788" y="631" font-size="18" text-anchor="middle">TEA</text>
  <text class="product-name" x="788" y="652" font-size="18" text-anchor="middle">FILTERS</text>

  <!-- Glue flap web address -->
  <line x1="1011" y1="475" x2="1011" y2="728" stroke="#6a6a6a" stroke-width="0.8"/>
  <line x1="1033" y1="475" x2="1033" y2="728" stroke="url(#goldSheen)" stroke-width="0.8"/>
  <text class="web-address" x="1022" y="604" text-anchor="middle" transform="rotate(-90 1022 604) translate(0 4)">WWW.LEAFHARBOR.EXAMPLE</text>
</svg>
</body>
</html>
```